Construction Business Card Design

We have a landscape construction company based in Australia
Were out of business cards ,
So now we're after a fresh looking modern card to give a fresh look to our business ....
We would like the business card to have the
(Front)
Tallow Ridge Pty Ltd
Director Gordon Marsh
0412563908
(Back)
Landscape,Construction,Paving,Excavation
(In smaller font low in the frame of card)
Different textures , curved edge , vertical and horizontal designs also minimal colours per design
Eg one side black , one coloured or a splash here or there
Industry/Entity Type
Landscape
Contact Information for Business Card
Tallow Ridge Pty Ltd
Director Gordon Marsh
0412563908
Landscape,Paving,Construction,Excavation

```html
<!DOCTYPE html>
<html lang="en">
<head>
<meta charset="utf-8">
<title>Tallow Ridge Pty Ltd – Business Card</title>
<link href="https://fonts.googleapis.com/css2?family=Open+Sans:wght@400;600&display=swap" rel="stylesheet">
<style>
  :root {
    --backdrop: #b4b7ba;
    --card-black: #000000;
    --leaf-green: #7dc242;
    --leaf-dark: #0e3a1c;
    --sky-blue: #15a6e3;
    --white: #ffffff;
    --tick-green: #2e9e3a;
  }
  * { margin: 0; padding: 0; box-sizing: border-box; }
  html, body {
    width: 1200px;
    height: 800px;
    overflow: hidden;
  }
  body {
    background: var(--backdrop);
    font-family: "Open Sans", Arial, sans-serif;
    position: relative;
  }
  .card {
    position: absolute;
    top: 130px;
    width: 330px;
    height: 540px;
    background: var(--card-black);
    border-radius: 0 64px 0 64px;
    overflow: hidden;
    box-shadow: 0 6px 18px rgba(0,0,0,0.25);
  }
  .card--front { left: 205px; }
  .card--back { left: 665px; }

  .leaf-pattern {
    position: absolute;
    inset: 0;
    background: radial-gradient(ellipse at 50% 55%, #0a2a14 0%, #061a0d 55%, #020805 100%);
  }

  .contact {
    position: absolute;
    top: 86px;
    left: 42px;
  }
  .contact__name {
    color: var(--leaf-green);
    font-size: 26px;
    font-weight: 400;
    line-height: 1.1;
  }
  .contact__role {
    color: var(--sky-blue);
    font-size: 13px;
    margin-top: 2px;
  }
  .contact__phone {
    color: var(--sky-blue);
    font-size: 21px;
    letter-spacing: 0.5px;
    margin-top: 0;
  }

  .brand-front {
    position: absolute;
    left: 42px;
    bottom: 48px;
    color: var(--sky-blue);
    font-size: 42px;
    font-weight: 400;
    line-height: 1;
  }
  .brand-front__suffix {
    display: block;
    font-size: 24px;
    text-align: right;
    margin-top: 4px;
  }

  .back-layout {
    position: absolute;
    width: 540px;
    height: 330px;
    left: -105px;
    top: 105px;
    transform: rotate(-90deg);
  }
  .brand-back {
    position: absolute;
    left: 0;
    right: 0;
    top: 108px;
    text-align: center;
    color: var(--sky-blue);
    font-size: 46px;
    font-weight: 400;
    line-height: 1;
  }
  .services {
    position: absolute;
    left: 0;
    right: 0;
    bottom: 58px;
    display: flex;
    justify-content: center;
    align-items: center;
    gap: 6px;
    color: var(--white);
    font-size: 19px;
    letter-spacing: 0.3px;
  }
  .services__tick { width: 12px; height: 12px; }
</style>
</head>
<body>

  <section class="card card--front" aria-label="Business card front">
    <div class="leaf-pattern" role="img" aria-label="Repeating dark green grass leaf pattern over black"></div>
    <div class="contact">
      <p class="contact__name">Gordon Marsh</p>
      <p class="contact__role">Director</p>
      <p class="contact__phone">0412563908</p>
    </div>
    <p class="brand-front">Tallow Ridge<span class="brand-front__suffix">Pty Ltd</span></p>
  </section>

  <section class="card card--back" aria-label="Business card back">
    <div class="back-layout">
      <p class="brand-back">Tallow Ridge Pty Ltd</p>
      <p class="services">
        <span>Landscape</span>
        <svg class="services__tick" viewBox="0 0 12 12" aria-hidden="true"><path d="M1 6 L5 10 L11 2" fill="none" stroke="var(--tick-green)" stroke-width="2"/></svg>
        <span>Construction</span>
        <svg class="services__tick" viewBox="0 0 12 12" aria-hidden="true"><path d="M1 6 L5 10 L11 2" fill="none" stroke="var(--tick-green)" stroke-width="2"/></svg>
        <span>Paving</span>
        <svg class="services__tick" viewBox="0 0 12 12" aria-hidden="true"><path d="M1 6 L5 10 L11 2" fill="none" stroke="var(--tick-green)" stroke-width="2"/></svg>
        <span>Excavation</span>
      </p>
    </div>
  </section>

</body>
</html>
```